Billboard for Lawyers who handle work accident cases

We need a billboard design for our law firm based in Queens, New York. The billboard is 8 by 10. The billboard is long and not wide.

Our firm focuses on work accidents. We are looking for a professional ad that will catch the attention of drivers and pedestrians passing by. The ad should be to the point.

I am attaching our picture and our logo for the ad. We like the idea of using the slogan "HURT AT WORK?" in English and Spanish "HERIDO EN EL TRABAJO?";

We want minimal writing on the billboard. Our telephone number should be included. The ad should say "Millions Recovered for our clients" It should also say "Attorney Advertisement" in small font in a discrete place. We would like use colors that match/coordinate the colors of our logo and/or picture but it is not required. The design should communicate serious/professional tone with a hint of modern/vibrant attorneys.

Once we have something to work with we will work with the designer for adjustments.

All people injured at work

Law Firm

Requirements
Must have
• Must have HURT AT WORK and HERIDO EN EL TRABAJO (Spanish) OR another similar catchphrase
• Must have "Millions recovered for our clients"
• Must have telephone number (718) 555-0193
• Must have website "tkbriefhall.com"
• Must have in small font "Attorney Advertisement"

```html
<!DOCTYPE html>
<html lang="en">
<head>
<meta charset="utf-8">
<title>Tavera &amp; Kemble — Hurt at Work Billboard</title>
<link href="https://fonts.googleapis.com/css2?family=Montserrat:wght@500;600;700&family=Cinzel:wght@600&display=swap" rel="stylesheet">
<style>
  :root {
    --page: #ffffff;
    --header: #ffffff;
    --gold: #a98a5a;
    --gold-dark: #8c7046;
    --stone-light: #cfc9bd;
    --stone-mid: #a39c90;
    --stone-dark: #6e675d;
    --footer: #3e342a;
    --suit: #1e2b52;
    --suit-deep: #17213f;
    --white: #ffffff;
  }
  * { box-sizing: border-box; margin: 0; padding: 0; }
  html, body { width: 1200px; height: 658px; overflow: hidden; background: var(--page); }
  .billboard {
    position: absolute; left: 348px; top: 14px;
    width: 504px; height: 630px;
    box-shadow: 0 6px 18px rgba(0,0,0,0.35);
    font-family: "Montserrat", Arial, sans-serif;
    color: var(--white);
    overflow: hidden;
  }
  .firm-header {
    position: absolute; left: 0; top: 0; width: 100%; height: 64px;
    background: var(--header);
    display: flex; flex-direction: column; align-items: center; justify-content: center;
  }
  .firm-name {
    font-family: "Cinzel", Georgia, serif; font-weight: 600;
    font-size: 17px; letter-spacing: 1px; color: var(--gold-dark); line-height: 1.1;
  }
  .firm-tagline {
    font-family: "Cinzel", Georgia, serif; font-weight: 600;
    font-size: 7px; letter-spacing: 2px; color: var(--gold-dark); margin-top: 2px;
  }
  .courthouse-backdrop {
    position: absolute; left: 0; top: 64px; width: 100%; height: 499px;
    background: linear-gradient(180deg, var(--stone-light) 0%, var(--stone-mid) 40%, var(--stone-dark) 100%);
  }
  .headline {
    position: absolute; left: 0; width: 100%; text-align: center;
    font-weight: 700; font-size: 33px; line-height: 1;
    text-shadow: 0 2px 4px rgba(0,0,0,0.45);
  }
  .headline-en { top: 91px; }
  .headline-es { top: 140px; }
  .disclaimer {
    position: absolute; top: 200px; left: 0; width: 100%; text-align: center;
    font-weight: 500; font-size: 17px; text-shadow: 0 1px 3px rgba(0,0,0,0.5);
  }
  .results-band {
    position: absolute; top: 248px; left: 0; width: 100%; height: 29px;
    background: var(--gold);
    display: flex; align-items: center; justify-content: center;
    font-weight: 600; font-size: 20px;
  }
  .attorneys-photo {
    position: absolute; left: 0; top: 292px; width: 100%; height: 271px;
    background:
      radial-gradient(ellipse 130px 120px at 25% 100%, var(--suit) 0%, var(--suit) 55%, rgba(30,43,82,0) 100%),
      radial-gradient(ellipse 130px 120px at 75% 100%, var(--suit) 0%, var(--suit) 55%, rgba(30,43,82,0) 100%),
      radial-gradient(ellipse 60px 75px at 25% 35%, #8a6e5c 0%, rgba(138,110,92,0) 100%),
      radial-gradient(ellipse 60px 75px at 75% 35%, #8a6e5c 0%, rgba(138,110,92,0) 100%),
      linear-gradient(180deg, #8f887c 0%, #6a6358 60%, #4a4850 100%);
  }
  .contact-bar {
    position: absolute; left: 0; bottom: 0; width: 100%; height: 67px;
    background: var(--footer);
    display: flex; align-items: center; justify-content: center; gap: 8px;
    font-weight: 700; font-size: 23px;
  }
  .contact-divider { font-weight: 500; }
</style>
</head>
<body>
  <div class="billboard">
    <header class="firm-header">
      <div class="firm-name">TAVERA &amp; KEMBLE</div>
      <div class="firm-tagline">ATTORNEYS AT LAW</div>
    </header>

    <div class="courthouse-backdrop" role="img" aria-label="Photograph of a courthouse facade with classical stone columns"></div>

    <h1 class="headline headline-en">HURT AT WORK</h1>
    <h2 class="headline headline-es">HERIDO EN EL TRABAJO</h2>
    <p class="disclaimer">Attorney Advertisement</p>
    <div class="results-band">Millions Recovered For Our Clients</div>

    <div class="attorneys-photo" role="img" aria-label="Portrait photograph of the two firm attorneys standing side by side in navy suits"></div>

    <footer class="contact-bar">
      <span class="contact-phone">(718) 555-0193</span>
      <span class="contact-divider">|</span>
      <span class="contact-web">tkbriefhall.com</span>
    </footer>
  </div>
</body>
</html>
```